Business Card/Email Signature design

We need an new business card design for our business as well as an animated email signature design.<br/>Business Card:<br/>The business card designs need to have the following information for each director:<br/>Leon Bramwell<br/>Managing Director<br/>leon@talvoraworks.com.au<br/>0498617340<br/>www.talvoraworks.com.au<br/><br/>and<br/><br/>Priscilla Venton<br/>Director<br/>priscilla@talvoraworks.com.au<br/>0467302958<br/>www.talvoraworks.com.au<br/><br/>I will upload the Talvora. Works logo designs to be used for the design. Our colours are black and white. I would like to see the designs in both coloured backgrounds.<br/><br/>For the email signature we need the same information. I also need to add a logo of our association BLPX of which i will add the logo as well. This BLPX logo does not need to be used for the business card unless it works with the design.<br/>For the animation part of the logo our company is called Talvora. Works - We have a number of divisions called Talvora. Construct, Talvora. Property, Talvora. Sales, Talvora. Executive Support, Talvora. Private PA, Talvora. Talent and Talvora. Coaching<br/>I would like for the email Signature to be designed so that the Talvora. stays still but the words Construct, Property, Sales, Executive Support, Private PA, Talent and Coaching rotate through to capture attention and tell the story of what we do.<br/><br/>Any questions please don't hesitate to message me.

Industry/Entity Type

Recruiter

Contact Information for Business Card

Leon Bramwell
Managing Director
leon@talvoraworks.com.au
0498617340
www.talvoraworks.com.au

Priscilla Venton
Director
priscilla@talvoraworks.com.au
0467302958
www.talvoraworks.com.au

Font styles to use
Serif

Colors

Designer to choose colors to be used in the design.

Requirements
Must have
• The animation for the email signature as described
Should not have
• Any changes to my logo. Any colour other that black or white

```html
<!DOCTYPE html>
<html lang="en">
<head>
<meta charset="utf-8">
<title>Talvora. Works — Business Card</title>
<link href="https://fonts.googleapis.com/css2?family=Lato:wght@300;400;700;900&display=swap" rel="stylesheet">
<style>
  :root {
    --ink: #0b0b0d;
    --paper: #ffffff;
    --muted: #6f6f73;
    --stage: #2b2b2e;
  }
  * { margin: 0; padding: 0; box-sizing: border-box; }
  html, body { width: 1200px; height: 900px; overflow: hidden; }
  body {
    background: var(--stage);
    font-family: "Lato", Arial, sans-serif;
    position: relative;
  }
  .card {
    position: absolute;
    width: 560px;
    height: 320px;
    border-radius: 16px;
    overflow: hidden;
  }
  .card--back { left: 90px; top: 80px; background: var(--ink); }
  .card--front { left: 550px; top: 480px; background: var(--paper); }

  .brand {
    position: absolute;
    display: flex;
    align-items: center;
    gap: 18px;
  }
  .brand__mark {
    flex: none;
    width: 80px; height: 80px;
    border: 1.5px solid currentColor;
  }
  .brand__name {
    white-space: nowrap;
    font-weight: 700;
    font-size: 28px;
    letter-spacing: 2px;
    text-transform: uppercase;
    padding-bottom: 8px;
    border-bottom: 1.5px solid currentColor;
  }
  .card--back .brand { color: var(--paper); left: 50%; top: 50%; transform: translate(-50%, -50%); }

  .card--front .brand {
    color: var(--ink);
    left: 44px; top: 96px;
    flex-direction: column;
    align-items: center;
    gap: 10px;
  }
  .card--front .brand__mark { width: 70px; height: 70px; }
  .card--front .brand__name { font-size: 20px; padding-bottom: 6px; }

  .person { position: absolute; right: 34px; top: 36px; text-align: right; }
  .person__name { font-weight: 900; font-size: 28px; color: var(--ink); white-space: nowrap; }
  .person__role { font-weight: 300; font-size: 15px; color: var(--muted); margin-top: 2px; }

  .wave { position: absolute; inset: 0; }

  .contacts {
    position: absolute;
    right: 22px;
    top: 214px;
    list-style: none;
    color: var(--paper);
    font-size: 13px;
    font-weight: 400;
  }
  .contacts li {
    display: flex;
    justify-content: flex-end;
    align-items: center;
    gap: 10px;
    height: 24px;
    white-space: nowrap;
  }
  .contacts svg { width: 15px; height: 15px; flex: none; }
</style>
</head>
<body>

<section class="card card--back">
  <div class="brand">
    <span class="brand__mark"></span>
    <span class="brand__name">Talvora. Works</span>
  </div>
</section>

<section class="card card--front">
  <svg class="wave" viewBox="0 0 560 320" aria-hidden="true">
    <path d="M0,320 L0,256 C130,300 230,290 300,230 C370,170 440,120 560,108 L560,320 Z" fill="var(--ink)"/>
    <path d="M0,268 C130,312 240,302 310,242 C365,195 420,150 480,128 C430,155 390,192 332,250 C255,322 130,322 0,288 Z" fill="var(--paper)"/>
  </svg>

  <div class="person">
    <div class="person__name">Leon Bramwell</div>
    <div class="person__role">Managing Director</div>
  </div>

  <div class="brand">
    <span class="brand__mark"></span>
    <span class="brand__name">Talvora. Works</span>
  </div>

  <ul class="contacts">
    <li>0498617340
      <svg viewBox="0 0 24 24"><path fill="#fff" d="M6.6 10.8a15 15 0 0 0 6.6 6.6l2.2-2.2a1 1 0 0 1 1-.25 11.4 11.4 0 0 0 3.6.57 1 1 0 0 1 1 1V20a1 1 0 0 1-1 1A17 17 0 0 1 3 4a1 1 0 0 1 1-1h3.5a1 1 0 0 1 1 1c0 1.25.2 2.45.57 3.57a1 1 0 0 1-.25 1z"/></svg>
    </li>
    <li>leon@talvoraworks.com.au
      <svg viewBox="0 0 24 24"><path d="M2 5h20v14H2z M3.5 6.5 12 13l8.5-6.5" fill="none" stroke="#fff" stroke-width="2"/></svg>
    </li>
    <li>www.talvoraworks.com.au
      <svg viewBox="0 0 24 24"><circle cx="12" cy="12" r="9" fill="none" stroke="#fff" stroke-width="2"/><path d="M3 12h18M12 3c3 3 3 15 0 18M12 3c-3 3-3 15 0 18" fill="none" stroke="#fff" stroke-width="1.5"/></svg>
    </li>
  </ul>
</section>

</body>
</html>
```